【依頼の目的/概要】
電子書籍(lumora)の表紙デザインをお願いします。

【画像サイズ】 ※RZBより抜粋
表紙ファイルの理想的な寸法 2,560×1,600ピクセルです。
注:画像の寸法は 1,000×625ピクセル以上であることが必要です。
画像の最大の寸法は 10,000×10,000ピクセルです。

【タイトル】

5つの航路・ヴォルテノ大年譜など
時代不変の必修名著群をサクっと1冊に凝縮しました

【著者】

RUNO

【本の内容】

5つの航路・ヴォルテノ大年譜などの人間心理・成功本を
まとめて解説した本です。

※本文を参考資料として添付します。

【デザイン要望】

特にイメージにこだわりはありませんので、
自由な発送でのデザインご応募を楽しみにしています。

※次点の方への参加報酬を設定致しました。

※その他 必要な情報がありましたら、お問い合わせください。

```html
<!DOCTYPE html>
<html lang="ja">
<head>
<meta charset="utf-8">
<title>時代不変の必修名著群をサクっと1冊に凝縮しました — RUNO</title>
<link rel="stylesheet" href="https://fonts.googleapis.com/css2?family=Noto+Sans+JP:wght@700;900&family=Roboto:wght@700&display=swap">
<style>
  :root {
    --cover-red: #e8285c;
    --title-white: #ffffff;
    --accent-yellow: #ffe600;
    --figure-dark: #2a2a2a;
  }
  html, body {
    margin: 0;
    padding: 0;
    width: 750px;
    height: 1200px;
    overflow: hidden;
    background: var(--cover-red);
  }
  .cover {
    position: relative;
    width: 750px;
    height: 1200px;
    background: var(--cover-red);
    font-family: "Noto Sans JP", sans-serif;
    overflow: hidden;
  }
  .series-line {
    position: absolute;
    top: 42px;
    left: 0;
    width: 750px;
    text-align: center;
    margin: 0;
    color: var(--accent-yellow);
    font-weight: 900;
    font-size: 44px;
    letter-spacing: 1px;
    line-height: 1.2;
  }
  .title {
    position: absolute;
    top: 130px;
    left: 0;
    width: 750px;
    margin: 0;
    color: var(--title-white);
    font-weight: 900;
    font-size: 104px;
    line-height: 126px;
    letter-spacing: 0;
  }
  .title-line {
    display: block;
    text-align: right;
    padding-right: 22px;
    white-space: nowrap;
  }
  .title-line--last {
    text-align: left;
    padding-left: 22px;
    padding-right: 0;
  }
  .title-accent {
    color: var(--accent-yellow);
  }
  .source-list {
    position: absolute;
    top: 895px;
    left: 30px;
    margin: 0;
    padding: 0;
    list-style: none;
    color: var(--title-white);
    font-family: "Roboto", sans-serif;
    font-weight: 700;
    font-size: 19px;
    line-height: 30px;
  }
  .thinker-figure {
    position: absolute;
    left: 470px;
    top: 730px;
    width: 260px;
    height: 330px;
    border-radius: 130px 130px 20px 20px;
    background: linear-gradient(160deg, #3a3a3a 0%, var(--figure-dark) 70%, #c8204f 100%);
  }
  .author {
    position: absolute;
    left: 30px;
    top: 1095px;
    margin: 0;
    color: var(--title-white);
    font-weight: 900;
    font-size: 46px;
    line-height: 1;
  }
  .author-suffix {
    font-size: 24px;
    font-weight: 700;
    margin-left: 6px;
  }
</style>
</head>
<body>
  <main class="cover">
    <p class="series-line">5つの航路・ヴォルテノ大年譜など</p>
    <h1 class="title">
      <span class="title-line">時代不変の</span>
      <span class="title-line"><span class="title-accent">必修名著群</span>を</span>
      <span class="title-line">サクっと1冊に</span>
      <span class="title-line title-line--last">凝縮しました</span>
    </h1>
    <ul class="source-list">
      <li>The 5 Routes of Highly Steady Voyagers</li>
      <li>individual psychology</li>
      <li>Harlen's hierarchy of needs</li>
      <li>Six human needs</li>
      <li>Volteno: A Grand Chronicle of Humankind</li>
    </ul>
    <div class="thinker-figure" role="img" aria-label="眼鏡をかけてペンを口元に当て、考え込む男性のイラスト"></div>
    <p class="author">RUNO<span class="author-suffix">著</span></p>
  </main>
</body>
</html>
```